Web Design Project - KornHaus.de

The page shall provide individual brown-bread mix.
There shall be presented:
* RECIPES: consumer's choice and feedback area
* EQUIPMENT: baking equipment store
* BREAD-MIX: individual mix and configurator function for bread-mix
The consumer can search/view the content and checkout the products. A user can establish a profile. A user can interact on the page for feedback on content and connection to social media.

```html
<!DOCTYPE html>
<html lang="en">
<head>
<meta charset="utf-8">
<title>KornHaus.de – About KornHaus</title>
<link href="https://fonts.googleapis.com/css2?family=Arimo:wght@400;700&display=swap" rel="stylesheet">
<style>
  :root {
    --brand: #b57a2c;
    --brand-dark: #9c6620;
    --header-top: #e6cc9c;
    --header-bottom: #f1e1c1;
    --crumb-bg: #f8f8f8;
    --text: #2a2a2a;
    --muted: #bdbdbd;
    --footer-top: #ead8bb;
    --footer-bottom: #f9f2e7;
    --social: #6f8fb8;
    --white: #ffffff;
  }
  * { box-sizing: border-box; margin: 0; padding: 0; }
  html, body { width: 1200px; height: 982px; overflow: hidden; }
  body {
    position: relative;
    background: var(--white);
    font-family: "Arimo", Arial, sans-serif;
    color: var(--text);
  }
  a { color: inherit; text-decoration: none; }

  /* Header */
  .site-header {
    position: absolute; left: 0; top: 0; width: 1200px; height: 185px;
    background: radial-gradient(ellipse 700px 300px at 280px 80px, #f6e8cc 0%, rgba(246,232,204,0) 70%),
                linear-gradient(180deg, var(--header-top), var(--header-bottom));
  }
  .brand-name {
    position: absolute; left: 109px; top: 44px;
    font-size: 52px; font-weight: 700; color: var(--brand); letter-spacing: -0.5px;
  }
  .social { position: absolute; display: flex; gap: 9px; }
  .social-icon { width: 28px; height: 28px; border-radius: 4px; background: var(--social); }
  .header-social { left: 830px; top: 22px; }
  .account-links {
    position: absolute; left: 912px; top: 25px;
    font-size: 19px; font-weight: 700; color: var(--brand);
    display: flex; gap: 8px; align-items: center;
  }
  .account-links .divider { font-weight: 400; }
  .main-nav {
    position: absolute; left: 111px; top: 138px;
    display: flex; gap: 33px; font-size: 19.5px; font-weight: 700; color: var(--brand);
  }
  .search {
    position: absolute; left: 783px; top: 133px; width: 305px; height: 34px;
    background: var(--white); border-radius: 17px; border: 1px solid #e2cfa8;
    display: flex; align-items: center; padding: 0 14px 0 17px;
    font-size: 14px; color: var(--brand);
  }
  .search span { flex: 1; }

  /* Breadcrumb */
  .breadcrumb {
    position: absolute; left: 0; top: 185px; width: 1200px; height: 42px;
    background: var(--crumb-bg); padding: 13px 0 0 115px;
    font-size: 14px; font-weight: 700;
  }
  .breadcrumb .sep { margin: 0 9px; }
  .breadcrumb .current { color: var(--brand); }

  /* Content */
  .page-title {
    position: absolute; left: 115px; top: 242px;
    font-size: 35px; font-weight: 700; color: var(--brand);
  }
  .product-visual {
    position: absolute; left: 60px; top: 325px; width: 470px; height: 340px;
    background: radial-gradient(ellipse 120px 160px at 230px 150px, #ecd2a4 0%, #f5e6cc 55%, rgba(255,255,255,0) 100%),
                radial-gradient(ellipse 220px 40px at 240px 290px, #e4e4e4 0%, rgba(255,255,255,0) 100%);
  }
  .benefits-title {
    position: absolute; left: 117px; top: 681px;
    font-size: 28px; font-weight: 700; color: var(--brand);
  }
  .benefits {
    position: absolute; left: 123px; top: 734px;
    display: grid; grid-template-columns: 149px 180px; row-gap: 11px;
    list-style: none; font-size: 17.5px; font-weight: 700; color: var(--text);
  }
  .benefits li { display: flex; align-items: center; gap: 12px; height: 20px; }
  .benefits svg { flex: none; }

  .intro {
    position: absolute; left: 509px; top: 327px; width: 585px;
  }
  .lead {
    font-size: 27px; font-weight: 700; line-height: 35px; color: var(--brand);
    margin-bottom: 43px;
  }
  .intro p.body-text {
    font-size: 13.6px; line-height: 24px; color: var(--text); margin-bottom: 24px;
  }

  /* Footer */
  .site-footer {
    position: absolute; left: 0; top: 919px; width: 1200px; height: 63px;
    background: linear-gradient(180deg, var(--footer-top), var(--footer-bottom));
    font-size: 14px; color: var(--brand);
  }
  .copyright { position: absolute; left: 109px; top: 25px; }
  .footer-nav { position: absolute; right: 196px; top: 25px; display: flex; gap: 20px; }
  .footer-social { left: 1023px; top: 18px; }
  .footer-social .social-icon { width: 26px; height: 26px; }
</style>
</head>
<body>
  <header class="site-header">
    <div class="brand-name">KornHaus.de</div>
    <div class="social header-social">
      <span class="social-icon" aria-label="Social network"></span>
      <span class="social-icon" aria-label="Social network"></span>
    </div>
    <div class="account-links">
      <a href="#">Join Now</a><span class="divider">|</span><a href="#">Login</a>
    </div>
    <nav class="main-nav">
      <a href="#">About KornHaus</a>
      <a href="#">Bread-Mix</a>
      <a href="#">Equipment</a>
      <a href="#">Recipes</a>
      <a href="#">Contact</a>
    </nav>
    <div class="search">
      <span>search, product, recipe</span>
      <svg width="18" height="18" viewBox="0 0 18 18" aria-hidden="true">
        <circle cx="7" cy="7" r="5.5" fill="none" stroke="#d8b888" stroke-width="2"/>
        <line x1="11" y1="11" x2="16" y2="16" stroke="#d8b888" stroke-width="2.5" stroke-linecap="round"/>
      </svg>
    </div>
  </header>

  <div class="breadcrumb">
    <a href="#">Home</a><span class="sep">&gt;</span><span class="current">About KornHaus</span>
  </div>

  <main>
    <h1 class="page-title">About KornHaus</h1>

    <div class="product-visual" role="img" aria-label="Product photo of a KornHaus bread-mix box"></div>

    <h2 class="benefits-title">KornHaus Health Benefits</h2>
    <ul class="benefits">
      <li><svg width="16" height="16" viewBox="0 0 16 16" aria-hidden="true"><circle cx="8" cy="8" r="7" fill="var(--muted)"/><path d="M4 8h6M8 5l3 3-3 3" fill="none" stroke="#fff" stroke-width="2"/></svg>Gluten Free</li>
      <li><svg width="16" height="16" viewBox="0 0 16 16" aria-hidden="true"><circle cx="8" cy="8" r="7" fill="var(--muted)"/><path d="M4 8h6M8 5l3 3-3 3" fill="none" stroke="#fff" stroke-width="2"/></svg>No Preservatives</li>
      <li><svg width="16" height="16" viewBox="0 0 16 16" aria-hidden="true"><circle cx="8" cy="8" r="7" fill="var(--muted)"/><path d="M4 8h6M8 5l3 3-3 3" fill="none" stroke="#fff" stroke-width="2"/></svg>Yeast Free</li>
      <li><svg width="16" height="16" viewBox="0 0 16 16" aria-hidden="true"><circle cx="8" cy="8" r="7" fill="var(--muted)"/><path d="M4 8h6M8 5l3 3-3 3" fill="none" stroke="#fff" stroke-width="2"/></svg>High in Fibre</li>
      <li><svg width="16" height="16" viewBox="0 0 16 16" aria-hidden="true"><circle cx="8" cy="8" r="7" fill="var(--muted)"/><path d="M4 8h6M8 5l3 3-3 3" fill="none" stroke="#fff" stroke-width="2"/></svg>Sugar Free</li>
      <li><svg width="16" height="16" viewBox="0 0 16 16" aria-hidden="true"><circle cx="8" cy="8" r="7" fill="var(--muted)"/><path d="M4 8h6M8 5l3 3-3 3" fill="none" stroke="#fff" stroke-width="2"/></svg>Low in Saturated Fat</li>
    </ul>

    <section class="intro">
      <p class="lead">Lorem ipsum dolor sit amet, consectetur adipis-icing elit, sed do eiusmod tempor incididunt ut labore et dolore magna aliqua.</p>
      <p class="body-text">Lorem ipsum dolor sit amet, consectetur adipisicing elit, sed do eiusmod tempor incididunt ut labore et dolore magna aliqua. Ut enim ad minim veniam, quis nostrud exercitation ullamco laboris nisi ut aliquip ex ea commodo consequat. Duis aute irure dolor in reprehenderit in voluptate velit esse cillum dolore eu fugiat nulla pariatur. Excepteur sint occaecat cupidatat non proident, sunt in culpa qui officia deserunt mollit anim id est laborum.</p>
      <p class="body-text">Lorem ipsum dolor sit amet, consectetur adipisicing elit, sed do eiusmod tempor incididunt ut labore et dolore magna aliqua. Ut enim ad minim veniam, quis nostrud exercitation ullamco laboris nisi ut aliquip ex ea commodo consequat. Duis aute irure dolor in reprehenderit in voluptate velit esse cillum dolore eu fugiat nulla pariatur. Excepteur sint occaecat cupidatat non proident, sunt in culpa qui officia deserunt mollit anim id est laborum.Lorem ipsum dolor sit amet, consectetur adipisicing elit, sed do eiusmod tempor incididunt ut labore et dolore magna aliqua. Ut enim ad minim veniam, quis nostrud exercitation ullamco laboris nisi ut aliquip ex ea commodo consequat. Duis aute irure dolor in reprehenderit in voluptate velit esse cillum dolore eu fugiat nulla pariatur.</p>
    </section>
  </main>

  <footer class="site-footer">
    <div class="copyright">© 2011 KornHaus, All Rights Reserved</div>
    <nav class="footer-nav">
      <a href="#">About KornHaus</a>
      <a href="#">Bread-Mix</a>
      <a href="#">Equipment</a>
      <a href="#">Recipes</a>
      <a href="#">Contact</a>
    </nav>
    <div class="social footer-social">
      <span class="social-icon" aria-label="Social network"></span>
      <span class="social-icon" aria-label="Social network"></span>
    </div>
  </footer>
</body>
</html>
```